Rapidly growing regional logistics company looking for a modern clean website design.

We need a website for a 5 year old company based in New England.
We offer a complete logistics solution. With services dedicated to the changing economic environment. Services to our customers include, same day delivery, trucking and van service, warehouse & storage, pool distribution, and B2B installations.
We've implemented leading technology along the way, that provides visibility, accountability, up to the minute tracking, and project management.
Our goal to be known in the industry we service as an excellent provider of time-critical services and dependability.
Independently of the services we offer, our customers know that they can count on a true partner.

Target Market(s)

B2B, including printers, retail, manufacturers, wholesalers, electronics, any company that needs product delivered or warehoused

Industry/Entity Type

Logistics

Coding

Coded - Design and coding required

Number of Pages Required

5+ page

Font styles to use
Sans Serif

Colors
0255a3

Requirements
Must have
• Clean, modern design, limited clutter. Limited tabs, preferred everything on 1st screen roll down to see info

```html
<!DOCTYPE html>
<html lang="en">
<head>
<meta charset="utf-8">
<title>Larkfield Logistics</title>
<link href="https://fonts.googleapis.com/css2?family=Open+Sans:wght@400;600;700;800&display=swap" rel="stylesheet">
<style>
:root{
  --brand:#0255a3;
  --brand-dark:#02458a;
  --ink:#222831;
  --body:#6a6f76;
  --line:#c9ccd1;
  --white:#ffffff;
  --footer-text:#dbe7f5;
}
*{margin:0;padding:0;box-sizing:border-box}
html,body{width:1200px;height:2757px;overflow:hidden;background:var(--white)}
body{font-family:"Open Sans",Arial,sans-serif;color:var(--body);position:relative}
.abs{position:absolute}

/* header */
.site-header{position:absolute;left:0;top:0;width:1200px;height:86px;background:var(--white);z-index:3}
.brand{position:absolute;left:112px;top:14px;display:flex;align-items:center;gap:12px}
.brand-dot{width:44px;height:44px;border-radius:50%;background:var(--brand)}
.brand-name{font-weight:700;font-size:22px;letter-spacing:1px;color:var(--brand);line-height:1.05}
.callbar{position:absolute;right:168px;top:18px;display:flex;align-items:center;gap:8px;font-size:10px;font-weight:600;color:var(--ink);white-space:nowrap}
.callbar .num{font-size:17px;font-weight:700;color:var(--brand)}
.icon-round{width:22px;height:22px;border-radius:50%;background:var(--brand);display:flex;align-items:center;justify-content:center}
.search-round{position:absolute;left:1046px;top:18px;width:22px;height:22px;border-radius:50%;background:var(--ink);display:flex;align-items:center;justify-content:center}
.main-nav{position:absolute;top:56px;left:594px;display:flex;font-size:11px;font-weight:700;color:var(--ink)}
.main-nav a{color:inherit;text-decoration:none;padding:4px 8px;margin-right:16px}
.main-nav a.active{background:var(--brand);color:var(--white)}

/* hero */
.hero{position:absolute;left:0;top:86px;width:1200px;height:552px;
  background:linear-gradient(180deg,#5d6a7e 0%,#a58a80 30%,#c9b3a3 42%,#8c949e 60%,#6e747c 100%)}
.hero-arrow{position:absolute;top:246px;width:38px;height:38px;background:rgba(20,24,30,.75);display:flex;align-items:center;justify-content:center}
.hero-title{position:absolute;left:693px;top:328px;font-size:49px;font-weight:800;line-height:54px;color:var(--white);letter-spacing:.5px}
.btn-solid{position:absolute;background:var(--brand);color:var(--white);font-weight:700;font-size:15px;display:flex;align-items:center;justify-content:center}

/* services */
.section-title{position:absolute;width:1200px;text-align:center;font-size:21px;font-weight:700;color:var(--brand)}
.title-rule{position:absolute;left:580px;width:40px;height:2px;background:var(--line)}
.service{position:absolute;top:765px;width:295px}
.service-photo{width:295px;height:205px}
.service h3{margin-top:28px;font-size:13px;font-weight:700;color:var(--ink);display:flex;align-items:center;gap:14px}
.service h3::before{content:"";width:10px;height:10px;background:var(--brand)}
.service p{margin:12px 0 0 24px;font-size:10.5px;line-height:16px;width:265px}
.btn-outline{display:inline-flex;align-items:center;justify-content:center;border:1.5px solid var(--brand);color:var(--brand);font-size:9px;font-weight:700;height:22px;padding:0 8px;background:var(--white)}
.service .btn-outline{margin:18px 0 0 24px}

/* about */
.about{position:absolute;left:0;top:1162px;width:1200px;height:397px;overflow:hidden}
.about-copy{position:absolute;left:132px;top:66px;width:480px;color:var(--white)}
.about-copy h2{font-size:21px;font-weight:700;margin-bottom:24px}
.about-copy p{font-size:14px;line-height:20px;margin-bottom:18px}
.about .btn-solid{left:138px;top:238px;width:140px;height:43px;border:1.5px solid var(--white);background:var(--brand-dark)}

/* features */
.feature-photo{position:absolute;width:449px;height:318px;box-shadow:0 8px 18px rgba(0,0,0,.28)}
.feature-copy{position:absolute;width:420px}
.feature-copy h3{font-size:13px;font-weight:700;color:var(--ink);margin-bottom:14px}
.feature-copy p{font-size:10.5px;line-height:16px;margin-bottom:20px}

/* footer */
.site-footer{position:absolute;left:0;top:2399px;width:1200px;height:358px;background:var(--brand);color:var(--footer-text)}
.footer-brand{position:absolute;left:130px;top:62px;width:160px;text-align:center}
.footer-brand .brand-dot{width:84px;height:84px;background:var(--white);margin:0 auto 14px}
.footer-brand .brand-name{color:var(--white);font-size:24px;font-weight:600}
.footer-col{position:absolute;top:64px;font-size:11px}
.footer-col h4{font-size:10px;font-weight:700;color:var(--white);margin-bottom:24px}
.contact-row{display:flex;gap:16px;line-height:17px;margin-bottom:16px}
.menu-list{list-style:none;line-height:17px}
.field{width:256px;height:30px;background:var(--white);margin-bottom:5px;font-size:10px;color:#777;padding:7px 12px}
.field.tall{height:54px;margin-top:3px}
.btn-submit{display:inline-flex;align-items:center;justify-content:center;width:86px;height:28px;border:2px solid var(--white);font-size:11px;font-weight:700;color:var(--white);margin-top:6px}
.follow{position:absolute;left:130px;top:288px;display:flex;align-items:center;gap:10px;font-size:9px;font-weight:700;color:var(--white)}
.social{width:30px;height:30px;border-radius:50%;background:#3a6fc4}
.follow .label{margin-right:20px}
.copyright{position:absolute;left:884px;top:292px;font-size:9px}
</style>
</head>
<body>

<header class="site-header">
  <div class="brand"><span class="brand-dot"></span><span class="brand-name">LARKFIELD<br>LOGISTICS</span></div>
  <div class="callbar">
    <span class="icon-round"><svg width="11" height="11" viewBox="0 0 24 24"><path fill="#fff" d="M6.6 10.8a15 15 0 0 0 6.6 6.6l2.2-2.2c.3-.3.7-.4 1-.2 1.1.4 2.3.6 3.6.6.6 0 1 .4 1 1V20c0 .6-.4 1-1 1A17 17 0 0 1 3 4c0-.6.4-1 1-1h3.5c.6 0 1 .4 1 1 0 1.3.2 2.5.6 3.6.1.3 0 .7-.2 1z"/></svg></span>
    <span>CALL US :</span><span class="num">555.010.2030</span>
  </div>
  <span class="search-round"><svg width="11" height="11" viewBox="0 0 24 24"><circle cx="10" cy="10" r="6" fill="none" stroke="#fff" stroke-width="3"/><path d="M15 15l6 6" stroke="#fff" stroke-width="3"/></svg></span>
  <nav class="main-nav">
    <a class="active">HOME</a><a>ABOUT US</a><a>SERVICES</a><a>BLOG</a><a>TESTIMONIALS</a><a style="margin-right:0">CONTACT</a>
  </nav>
</header>

<section class="hero" role="img" aria-label="Photo of orange semi trucks parked at a warehouse loading yard under an evening sky">
  <div class="hero-arrow" style="left:0"><svg width="10" height="14" viewBox="0 0 10 14"><path d="M8 1L2 7l6 6" fill="none" stroke="#fff" stroke-width="2"/></svg></div>
  <div class="hero-arrow" style="right:0"><svg width="10" height="14" viewBox="0 0 10 14"><path d="M2 1l6 6-6 6" fill="none" stroke="#fff" stroke-width="2"/></svg></div>
  <h1 class="hero-title">LOGISTICS<br>SOLUTION</h1>
  <a class="btn-solid" style="left:698px;top:453px;width:138px;height:42px">READ MORE</a>
</section>

<h2 class="section-title" style="top:676px">OUR SERVICES</h2>
<div class="title-rule" style="top:719px"></div>

<article class="service" style="left:130px">
  <div class="service-photo" role="img" aria-label="Photo of a warehouse aisle with blue and orange pallet racking" style="background:linear-gradient(180deg,#c97a45 0%,#3d62a8 45%,#b9a58a 100%)"></div>
  <h3>WAREHOUSING</h3>
  <p>Our warehouse facility may prove to be one<br>of the most valuable extensions of your<br>company's operations.</p>
  <a class="btn-outline">READ MORE</a>
</article>
<article class="service" style="left:456px">
  <div class="service-photo" role="img" aria-label="Photo of white cargo vans driving on a highway" style="background:linear-gradient(180deg,#7fb2e3 0%,#bcd7ee 45%,#8b8f79 70%,#5b5d58 100%)"></div>
  <h3>TRUCK &amp; VAN SERVICE</h3>
  <p>Rush and pre-scheduled delivery<br>Light and heavy trucking (cargo vans to liftgates)<br>Expedited ground services</p>
  <a class="btn-outline">READ MORE</a>
</article>
<article class="service" style="left:774px">
  <div class="service-photo" role="img" aria-label="Photo of an orange forklift moving boxes in a warehouse" style="background:linear-gradient(180deg,#9aa0a6 0%,#c7a77f 45%,#d46a36 75%,#8d8479 100%)"></div>
  <h3>DISTRIBUTION &amp; POOL SERVICES</h3>
  <p>Pool Distribution is the distribution of product<br>to numerous customers within a particular<br>geographic region.</p>
  <a class="btn-outline">READ MORE</a>
</article>

<section class="about">
  <div class="abs" role="img" aria-label="Photo of an open road through green fields under a blue sky" style="inset:0;background:linear-gradient(180deg,#2f78c4 0%,#5a93cf 55%,#3e5566 100%)"></div>
  <svg class="abs" style="left:0;top:0" width="1200" height="397" viewBox="0 0 1200 397">
    <circle cx="1040" cy="300" r="406" fill="none" stroke="#ffffff" stroke-width="18"/>
    <circle cx="1040" cy="300" r="392" fill="none" stroke="#0255a3" stroke-width="12"/>
    <circle cx="1040" cy="300" r="386" fill="#c9d8e8" role="img" aria-label="Photo of white delivery trucks and vans parked on a road"/>
  </svg>
  <div class="about-copy">
    <h2>ABOUT US</h2>
    <p>Our company was founded in 2012 but our team is seasoned,<br>with a combined 75 years of experience.</p>
    <p>Larkfield Logistics offers a complete logistics solution. With services<br>dedicated to the changing economic environment.</p>
  </div>
  <a class="btn-solid">READ MORE</a>
</section>

<div class="feature-photo" role="img" aria-label="Photo of a smiling courier in a blue uniform carrying parcels beside a yellow van" style="left:130px;top:1627px;background:linear-gradient(120deg,#e8c33a 0%,#d9b33a 35%,#2a62b8 60%,#c9a27a 85%,#e9e9e9 100%)"></div>
<div class="feature-copy" style="left:647px;top:1724px">
  <h3>SAME-DAY DELIVERY SERVICE</h3>
  <p>Regardless of the specifics of your needs, LARKFIELD can handle your same-day delivery needs. Larkfield Logistics offers same-day delivery services as a standalone service</p>
  <a class="btn-outline">READ MORE</a>
</div>

<div class="feature-copy" style="left:156px;top:2105px">
  <h3>DEDICATED DELIVERY SERVICE</h3>
  <p>Our goal is to make the process easy, and of course, to make you look good in the eyes of your customers and suppliers. Whether your needs are a car to tractor trailer Larkfield can provide the solution for you.</p>
  <a class="btn-outline">READ MORE</a>
</div>
<div class="feature-photo" role="img" aria-label="Photo of a courier handing a cardboard box to a customer at a doorway" style="left:601px;top:2007px;background:linear-gradient(110deg,#6d8f5a 0%,#c9d2c2 35%,#c99c6a 55%,#1f3f78 78%,#e8ecef 100%)"></div>

<footer class="site-footer">
  <div class="footer-brand"><div class="brand-dot"></div><div class="brand-name">LARKFIELD<br>LOGISTICS</div></div>

  <div class="footer-col" style="left:371px;width:220px">
    <h4>CONTACT US</h4>
    <div class="contact-row"><svg width="10" height="14" viewBox="0 0 10 14"><path d="M5 0a5 5 0 0 0-5 5c0 4 5 9 5 9s5-5 5-9a5 5 0 0 0-5-5zm0 7a2 2 0 1 1 0-4 2 2 0 0 1 0 4z" fill="#fff"/></svg><span>218 Alder Road, Milford,<br>NH 03055</span></div>
    <div class="contact-row"><svg width="12" height="12" viewBox="0 0 24 24"><path fill="#fff" d="M6.6 10.8a15 15 0 0 0 6.6 6.6l2.2-2.2c.3-.3.7-.4 1-.2 1.1.4 2.3.6 3.6.6.6 0 1 .4 1 1V20c0 .6-.4 1-1 1A17 17 0 0 1 3 4c0-.6.4-1 1-1h3.5c.6 0 1 .4 1 1 0 1.3.2 2.5.6 3.6.1.3 0 .7-.2 1z"/></svg><span>555.010.2030</span></div>
    <div class="contact-row"><svg width="12" height="10" viewBox="0 0 12 10"><rect width="12" height="10" rx="1" fill="#fff"/><path d="M0 1l6 4 6-4" fill="none" stroke="#0255a3" stroke-width="1.2"/></svg><span>info@larkfieldlogistics.com</span></div>
  </div>

  <div class="footer-col" style="left:630px">
    <h4>MENU</h4>
    <ul class="menu-list"><li>Home</li><li>About Us</li><li>Services</li><li>Blog</li><li>Contact us</li></ul>
  </div>

  <div class="footer-col" style="left:814px">
    <h4>QUICK CONTACT</h4>
    <div class="field" style="margin-top:-8px">Name</div>
    <div class="field">E mail</div>
    <div class="field tall">Message</div>
    <a class="btn-submit">SUBMIT</a>
  </div>

  <div class="follow"><span class="label">FOLLOW US</span><span class="social"></span><span class="social"></span><span class="social"></span></div>
  <div class="copyright">Copyrights @ 2017 All Rights Reserved</div>
</footer>

</body>
</html>
```